Personal Trainer Business Card Design and Logo

I am a Personal Trainer and passionate in helping obese kids loose weight, I would love a business card design for my business called LORK Fitness.
LORK Ftiness stands for Lively Origami Running Kicks, I would like the business card to be bright and appealing to the kids as well as the parents.
I would also love a logo designs witch is simple but affective.

Things I would like in the business card
- Kids playing and being happy (no cartoon characters)
- The card should be bright and colourful
- My name, Bartholomew Van Rijk Personal Trainer
- Contact number 0472618059
- Email address lorkfitness@mailzorp.com

Things I would like in the logo
-colourful design which incorporate kids
- your creative logo

thanks for all your entries
kind regards Bart

loving all the designs, you are all so talented.

could you please read the updated brief

kind regards

Bart

Reason: Loving the designs, but needs more modification kind reagrds Bart

Target Market(s)

Kids and Parents

Industry/Entity Type

Business

Contact Information for Business Card

LORK Fitness for kids

Lively Origami Running Kicks

Bart Van Rijk Personal Trainer
0472618059

Requirements
Must have
• Kids laughing and happy, lork fitness logo, Bart Van Rijk Personal Trainer, 0472618059,lorkfitness@mailzorp.com, colourful and bright.
Nice to have
• pulsewell council tick

```html
<!DOCTYPE html>
<html lang="en">
<head>
<meta charset="utf-8">
<title>LORK Fitness for Kids – Business Cards</title>
<link rel="stylesheet" href="https://fonts.googleapis.com/css2?family=Arimo:wght@700&family=Open+Sans:wght@400;600;700&family=Comic+Neue:wght@700&display=swap">
<style>
  :root {
    --page: #ffffff;
    --green-deep: #3a9a1e;
    --green-light: #a9d25e;
    --orange: #f39a12;
    --orange-text: #f07f12;
    --white: #ffffff;
    --ink: #2b2b2b;
    --ink-soft: #3d3d3d;
    --sky-top: #3f8fe0;
    --sky-bottom: #a9d4f5;
    --badge-green: #2f8d20;
    --badge-blue: #1f9fde;
    --badge-orange: #f08a1c;
    --tagline: rgba(255, 255, 255, 0.38);
  }
  * { margin: 0; padding: 0; box-sizing: border-box; }
  html, body {
    width: 1200px; height: 833px; overflow: hidden;
    background: var(--page);
  }
  .sheet { position: relative; width: 1200px; height: 833px; }
  .card {
    position: absolute; width: 514px; height: 316px;
    border-radius: 16px; overflow: hidden;
    box-shadow: 0 4px 10px rgba(0, 0, 0, 0.35);
  }
  .card--front { left: 58px; top: 65px; }
  .card--green { left: 619px; top: 62px; }
  .card--blue { left: 55px; top: 433px; }
  .card--orange { left: 622px; top: 432px; }
  .card-art { position: absolute; inset: 0; width: 514px; height: 316px; display: block; }

  .brand { position: absolute; font-family: "Arimo", Arial, sans-serif; font-weight: 700; line-height: 1; }
  .brand-name { color: var(--white); font-size: 28px; text-shadow: 1px 1px 2px rgba(0,0,0,0.45); }
  .brand-sub { color: var(--orange-text); font-size: 33px; text-shadow: 1px 1px 2px rgba(0,0,0,0.35); }
  .card--front .brand-name { right: 27px; top: 231px; }
  .card--front .brand-sub { right: 70px; top: 263px; }
  .card-back .brand-name { left: 0; width: 514px; padding-left: 130px; text-align: center; top: 14px; }
  .card-back .brand-sub { left: 0; width: 514px; padding-left: 130px; text-align: center; top: 46px; }

  .badge {
    position: absolute; left: 19px; top: 95px; width: 112px; height: 112px;
    border-radius: 50%; display: flex; align-items: center; justify-content: center;
    font-family: "Open Sans", Arial, sans-serif; font-weight: 700; font-size: 15px;
    color: var(--white); text-align: center; line-height: 1.2;
  }
  .card--green .badge { background: var(--badge-green); }
  .card--blue .badge { background: var(--badge-blue); }
  .card--orange .badge { background: var(--badge-orange); }

  .contact { position: absolute; left: 235px; top: 95px; font-family: "Open Sans", Arial, sans-serif; color: var(--ink-soft); }
  .contact-name { font-size: 18px; font-weight: 700; color: var(--ink); line-height: 24px; }
  .contact-role { font-size: 16px; line-height: 26px; }
  .contact-line { display: flex; align-items: center; gap: 8px; font-size: 16px; line-height: 27px; }
  .contact-line--phone { font-weight: 700; font-size: 17px; color: var(--ink); }
  .contact-icon { width: 14px; height: 14px; flex: none; }

  .tagline {
    position: absolute; font-family: "Comic Neue", "Comic Sans MS", cursive;
    font-weight: 700; font-size: 25px; color: var(--tagline); white-space: nowrap;
  }
  .tagline--left { left: 165px; top: 250px; transform: rotate(-12deg); transform-origin: left bottom; }
  .tagline--right { left: 325px; top: 260px; transform: rotate(8deg); transform-origin: left top; }
</style>
</head>
<body>
<main class="sheet">
  <svg width="0" height="0" style="position:absolute">
    <defs>
      <radialGradient id="greenField" cx="0.55" cy="0.45" r="0.7">
        <stop offset="0" stop-color="#b3d96a"/>
        <stop offset="0.6" stop-color="#6eb53a"/>
        <stop offset="1" stop-color="#3a9a1e"/>
      </radialGradient>
      <linearGradient id="sky" x1="0" y1="0" x2="0" y2="1">
        <stop offset="0" stop-color="#3f8fe0"/>
        <stop offset="1" stop-color="#a9d4f5"/>
      </linearGradient>
      <symbol id="iconPhone" viewBox="0 0 14 14"><rect x="3" y="0.5" width="8" height="13" rx="1.5" fill="none" stroke="#2b2b2b" stroke-width="1.4"/><line x1="3" y1="10.5" x2="11" y2="10.5" stroke="#2b2b2b" stroke-width="1.2"/></symbol>
      <symbol id="iconMail" viewBox="0 0 14 14"><rect x="0.7" y="3" width="12.6" height="8.5" fill="none" stroke="#2b2b2b" stroke-width="1.2"/><path d="M0.7 3 L7 8 L13.3 3" fill="none" stroke="#2b2b2b" stroke-width="1.2"/></symbol>
      <symbol id="iconWeb" viewBox="0 0 14 14"><circle cx="7" cy="7" r="6" fill="none" stroke="#2b2b2b" stroke-width="1.2"/><ellipse cx="7" cy="7" rx="2.6" ry="6" fill="none" stroke="#2b2b2b" stroke-width="1"/><line x1="1" y1="7" x2="13" y2="7" stroke="#2b2b2b" stroke-width="1"/></symbol>
      <symbol id="backArt" viewBox="0 0 514 316">
        <rect width="514" height="316" fill="url(#greenField)"/>
        <path d="M0 0 H92 Q178 150 88 316 H0 Z" fill="#ffffff"/>
        <path d="M106 0 Q192 150 100 316" fill="none" stroke="#f39a12" stroke-width="7"/>
      </symbol>
    </defs>
  </svg>

  <section class="card card--front">
    <svg class="card-art" viewBox="0 0 514 316">
      <rect width="514" height="316" fill="url(#sky)" role="img" aria-label="Photo of happy kids jumping in the air on a grassy field under a blue sky"/>
      <path d="M0 268 Q240 200 514 208 V316 H0 Z" fill="url(#greenField)"/>
      <path d="M0 268 Q240 200 514 208" fill="none" stroke="#f39a12" stroke-width="6"/>
    </svg>
    <div class="brand brand-name">LORK fitness</div>
    <div class="brand brand-sub">for kids</div>
  </section>

  <section class="card card-back card--green">
    <svg class="card-art"><use href="#backArt"/></svg>
    <div class="badge">LORK<br>Fitness</div>
    <div class="brand brand-name">LORK fitness</div>
    <div class="brand brand-sub">for kids</div>
    <div class="contact">
      <div class="contact-name">Bart Van Rijk</div>
      <div class="contact-role">Personal Trainer</div>
      <div class="contact-line contact-line--phone"><svg class="contact-icon"><use href="#iconPhone"/></svg>0472618059</div>
      <div class="contact-line"><svg class="contact-icon"><use href="#iconMail"/></svg>lorkfitness@mailzorp.com</div>
      <div class="contact-line"><svg class="contact-icon"><use href="#iconWeb"/></svg>lorkfitness.com.au</div>
    </div>
    <div class="tagline tagline--left">Lively Origami</div>
    <div class="tagline tagline--right">Running Kicks</div>
  </section>

  <section class="card card-back card--blue">
    <svg class="card-art"><use href="#backArt"/></svg>
    <div class="badge">LORK<br>Fitness</div>
    <div class="brand brand-name">LORK fitness</div>
    <div class="brand brand-sub">for kids</div>
    <div class="contact">
      <div class="contact-name">Bart Van Rijk</div>
      <div class="contact-role">Personal Trainer</div>
      <div class="contact-line contact-line--phone"><svg class="contact-icon"><use href="#iconPhone"/></svg>0472618059</div>
      <div class="contact-line"><svg class="contact-icon"><use href="#iconMail"/></svg>lorkfitness@mailzorp.com</div>
      <div class="contact-line"><svg class="contact-icon"><use href="#iconWeb"/></svg>lorkfitness.com.au</div>
    </div>
    <div class="tagline tagline--left">Lively Origami</div>
    <div class="tagline tagline--right">Running Kicks</div>
  </section>

  <section class="card card-back card--orange">
    <svg class="card-art"><use href="#backArt"/></svg>
    <div class="badge">LORK<br>Fitness</div>
    <div class="brand brand-name">LORK fitness</div>
    <div class="brand brand-sub">for kids</div>
    <div class="contact">
      <div class="contact-name">Bart Van Rijk</div>
      <div class="contact-role">Personal Trainer</div>
      <div class="contact-line contact-line--phone"><svg class="contact-icon"><use href="#iconPhone"/></svg>0472618059</div>
      <div class="contact-line"><svg class="contact-icon"><use href="#iconMail"/></svg>lorkfitness@mailzorp.com</div>
      <div class="contact-line"><svg class="contact-icon"><use href="#iconWeb"/></svg>lorkfitness.com.au</div>
    </div>
    <div class="tagline tagline--left">Lively Origami</div>
    <div class="tagline tagline--right">Running Kicks</div>
  </section>
</main>
</body>
</html>
```